Velmora.io amazing image design

This is *not* a logo! We need a typography design for the phrase "what makes you, you?" to capture people's attention when a user posts their psychological test results to QP.
We need the design to stand out and color to make it grab attention. Font should not be anything like Comic Sans! Think Tomas Brellinger!!!
Image needs to be sized and optimized for typical QP post (1200x630).

check us out at velmora.io

Target Market(s)

social media. as in, everyone who wants to learn more about themselves

Industry/Entity Type

Management Consulting

Logo Text

what makes you, you?

Colors

Designer to choose colors to be used in the design.

Requirements
Must have
• impact, originality, irony.
Nice to have
• an arresting image or colors
Should not have
• comic sans. dullness. sameness.

```html
<!DOCTYPE html>
<html lang="en">
<head>
<meta charset="utf-8">
<title>What makes you, you?</title>
<link rel="stylesheet" href="https://fonts.googleapis.com/css2?family=Bungee+Inline&display=swap">
<style>
  :root {
    --paper-dark: #141414;
    --paper-mid: #232323;
    --paper-light: #303030;
    --ink-white: #f6f2ef;
    --ink-black: #0b0b0b;
    --paint-yellow: #f2d21a;
    --paint-lime: #c9e04a;
    --paint-cyan: #2bb8c9;
    --paint-pink: #e4378f;
    --paint-orange: #f08a24;
  }
  html, body {
    margin: 0;
    padding: 0;
    overflow: hidden;
    background: var(--paper-dark);
  }
  .poster {
    position: relative;
    width: 1200px;
    height: 960px;
    overflow: hidden;
    background:
      radial-gradient(ellipse 420px 260px at 180px 140px, var(--paper-light), transparent 70%),
      radial-gradient(ellipse 380px 300px at 320px 720px, var(--paper-mid), transparent 70%),
      radial-gradient(ellipse 300px 220px at 1050px 880px, var(--paper-light), transparent 70%),
      linear-gradient(160deg, var(--paper-mid), var(--paper-dark) 55%, var(--paper-mid));
  }
  .torn-window {
    position: absolute;
    inset: 0;
    width: 1200px;
    height: 960px;
  }
  .headline {
    position: absolute;
    left: 36px;
    top: 118px;
    margin: 0;
    font-family: "Bungee Inline", "Arial Black", sans-serif;
    font-weight: 400;
    font-size: 168px;
    line-height: 180px;
    letter-spacing: -4px;
    color: var(--ink-white);
    text-transform: uppercase;
    text-shadow: 5px 5px 0 var(--ink-black);
  }
  .headline span {
    display: block;
  }
  .headline .line-you-comma {
    padding-left: 150px;
  }
  .headline .line-you-question {
    padding-left: 150px;
  }
</style>
</head>
<body>
  <main class="poster">
    <svg class="torn-window" viewBox="0 0 1200 960" aria-hidden="false">
      <defs>
        <linearGradient id="paint-tones" x1="0" y1="0" x2="1" y2="1">
          <stop offset="0" stop-color="var(--paint-lime)"/>
          <stop offset="0.3" stop-color="var(--paint-yellow)"/>
          <stop offset="0.5" stop-color="var(--paint-orange)"/>
          <stop offset="0.7" stop-color="var(--paint-cyan)"/>
          <stop offset="1" stop-color="var(--paint-pink)"/>
        </linearGradient>
      </defs>
      <polygon class="torn-edge" fill="#dcd6cf"
        points="741,70 842,90 1002,104 1154,119 1206,246 1206,336 1134,346 1066,414 996,444 1006,512 1066,650 1046,764 984,806 904,876 806,966 646,966 574,904 554,822 534,720 539,558 596,474 654,444 694,278 724,196 756,126"/>
      <polygon class="painted-portrait" role="img"
        aria-label="Close-up photograph of a laughing face covered in bright yellow, cyan and pink powder paint, seen through a tear in black paper"
        fill="url(#paint-tones)"
        points="745,75 840,95 1000,110 1150,125 1200,250 1200,330 1130,340 1060,410 990,440 1000,510 1060,650 1040,760 980,800 900,870 800,960 650,960 580,900 560,820 540,720 545,560 600,480 660,450 700,280 730,200 760,130"/>
    </svg>
    <h1 class="headline">
      <span class="line-what">What</span>
      <span class="line-makes">Makes</span>
      <span class="line-you-comma">You,</span>
      <span class="line-you-question">You?</span>
    </h1>
  </main>
</body>
</html>
```